New Signage Design Project

Real estate company looking for signage, PowerPoint and stationery branding. Signs will be placed in front of homes and other properties being sold

Name of company is Tern Haven, LLC

Requirements
Must have
• Name of company - Tern Haven, LLC

```html
<!DOCTYPE html>
<html lang="en">
<head>
<meta charset="utf-8">
<title>Tern Haven, LLC — For Sale Sign</title>
<link rel="stylesheet" href="https://fonts.googleapis.com/css2?family=Quicksand:wght@500&family=Roboto:wght@700;900&display=swap">
<style>
  :root {
    --canvas-bg: #eef0f2;
    --sign-white: #ffffff;
    --brand-navy: #13284f;
    --sale-red: #ec3238;
    --rule-grey: #9a9a9a;
  }
  * { margin: 0; padding: 0; box-sizing: border-box; }
  html, body {
    width: 1200px;
    height: 1200px;
    overflow: hidden;
    background: var(--canvas-bg);
  }
  .canvas {
    position: relative;
    width: 1200px;
    height: 1200px;
  }
  .sign {
    position: absolute;
    left: 50px;
    top: 241px;
    width: 1100px;
    height: 717px;
    background: var(--sign-white);
    overflow: hidden;
  }
  .brand {
    position: absolute;
    left: 0;
    right: 0;
    top: 150px;
    text-align: center;
    font-family: "Quicksand", sans-serif;
    font-weight: 500;
    font-size: 112px;
    line-height: 1;
    color: var(--brand-navy);
    letter-spacing: 1px;
  }
  .divider {
    position: absolute;
    left: 8px;
    right: 8px;
    top: 348px;
    height: 3px;
    background: var(--rule-grey);
  }
  .headline {
    position: absolute;
    left: 0;
    right: 0;
    top: 362px;
    text-align: center;
    font-family: "Roboto", sans-serif;
    font-weight: 900;
    font-size: 214px;
    line-height: 1;
    color: var(--sale-red);
    letter-spacing: 2px;
  }
  .contact-band {
    position: absolute;
    left: 0;
    right: 0;
    bottom: 0;
    height: 120px;
    background: var(--brand-navy);
    display: flex;
    align-items: center;
    justify-content: center;
  }
  .phone {
    font-family: "Roboto", sans-serif;
    font-weight: 700;
    font-size: 92px;
    line-height: 1;
    color: var(--sign-white);
    letter-spacing: 2px;
    white-space: pre;
  }
</style>
</head>
<body>
  <main class="canvas">
    <section class="sign" aria-label="For sale yard sign">
      <div class="brand">Tern Haven, LLC</div>
      <div class="divider"></div>
      <h1 class="headline">FOR SALE</h1>
      <div class="contact-band">
        <p class="phone">014 - 555 - 0172</p>
      </div>
    </section>
  </main>
</body>
</html>
```